Fernwick Hollow Craft Cannabis Company

We need a one-page website designed for a craft cannabis website called "Fernwick Hollow is a craft cannabis company" that will provide high-quality strains. It's located on 20 acres in Marrow Bay, Cedar Valley on lush green acreage. The facility takes pride in its modern technology bloom rooms to contain a healthy environment for high-quality handcrafted cannabis. We need a design that looks modern yet rustic- please do not add any marijuana leaves- We want the site to look professional as it is for investors. we will be selling products and do need the site to say "Coming soon"
Target Market(s)
investors and customers
Number of Pages Required
1 page
Font styles to use
Colors
Designer to choose colors to be used in the design.
Requirements
Must have
- greenery- its a cannabis production site with state of the art technology for growing. from seeds to full production it is a craft site with smaller rooms but high-end quality products. we need a tab that has a purchasing section another one for investors to watch our market trends and a page with our mission/ values and visions-
Nice to have
- showing people/ high end images/ greenspace/ farm (horticulture based)
Should not have
- no marijuana leaves

```html
<!DOCTYPE html>
<html lang="en">
<head>
<meta charset="utf-8">
<title>Fernwick Hollow Craft Cannabis Company</title>
<link rel="stylesheet" href="https://fonts.googleapis.com/css2?family=Montserrat:wght@500;600;700&family=Raleway:wght@300;400;500&family=Dancing+Script:wght@600&family=Lato:wght@400;700&display=swap">
<style>
:root{
  --green:#6cc41a;
  --ink:#1e1e1e;
  --grey:#555;
  --footer-bar:#4d4b4c;
  --white:#fff;
  --hero-top:#5d6a5c;
  --hero-bottom:#243a14;
}
*{margin:0;padding:0;box-sizing:border-box}
html,body{width:755px;height:1200px;overflow:hidden;background:var(--white)}
body{position:relative;font-family:"Raleway",sans-serif;color:var(--grey)}
h1,h2,h3{font-weight:400}

/* header */
.site-header{position:absolute;left:0;top:0;width:755px;height:79px;background:var(--white)}
.brand{position:absolute;left:36px;top:24px;width:130px;text-align:center;white-space:nowrap;font-family:"Montserrat",sans-serif;font-weight:600;font-size:12px;line-height:15px;color:var(--ink)}
.main-nav{position:absolute;top:34px;left:0;font-size:8px;color:var(--grey)}
.main-nav a{position:absolute;white-space:nowrap;color:inherit;text-decoration:none}
.main-nav a.active{color:var(--green);font-weight:500}
.shop-btn{position:absolute;left:637px;top:29px;width:66px;height:20px;background:var(--green);color:var(--white);font-family:"Montserrat",sans-serif;font-size:8px;text-align:center;line-height:20px;letter-spacing:.2px}

/* hero */
.hero{position:absolute;left:0;top:79px;width:755px;height:422px;background:linear-gradient(180deg,var(--hero-top) 0%,#4d5d45 35%,#334d22 60%,var(--hero-bottom) 100%)}
.hero-text{position:absolute;left:0;width:755px;text-align:center;color:var(--white)}
.hero-welcome{top:149px;font-family:"Dancing Script",cursive;font-size:13px}
.hero-title{top:172px;font-family:"Montserrat",sans-serif;font-weight:700;font-size:25px}
.hero-sub{top:209px;font-family:"Raleway",sans-serif;font-weight:300;font-size:16px}
.hero-status{top:264px;font-family:"Montserrat",sans-serif;font-weight:700;font-size:15px}
.dots{position:absolute;top:380px;left:361px}
.dot{position:absolute;top:0;width:6px;height:6px;border-radius:50%;border:1px solid var(--white)}
.dot.on{background:var(--white)}

/* about */
.about-title{position:absolute;top:560px;left:0;width:755px;text-align:center;font-family:"Raleway",sans-serif;font-weight:400;font-size:19px;color:var(--green)}
.about-rule{position:absolute;top:592px;left:365px;width:25px;height:1px;background:var(--grey)}
.about-photo{position:absolute;left:119px;top:631px;width:243px;height:163px;border:1px solid #333;background:linear-gradient(180deg,#d9e0dc 0%,#b9c6bd 40%,#6f9a4e 70%,#3f6e25 100%)}
.about-copy{position:absolute;left:394px;top:630px;width:241px;font-size:7.6px;line-height:14px;text-align:justify;color:var(--grey)}
.about-copy p+p{margin-top:12px}
.read-more{position:absolute;left:394px;top:773px;width:74px;height:20px;background:var(--green);color:var(--white);font-size:8px;text-align:center;line-height:20px}

/* footer */
.grass{position:absolute;left:0;top:868px;width:755px;height:70px;background:linear-gradient(180deg,rgba(108,196,26,0) 0%,rgba(108,196,26,.55) 45%,var(--green) 100%)}
.site-footer{position:absolute;left:0;top:937px;width:755px;height:216px;background:var(--green);color:var(--white);font-family:"Lato",sans-serif}
.foot-brand{position:absolute;left:48px;top:56px;width:130px;text-align:center;white-space:nowrap;font-family:"Montserrat",sans-serif;font-weight:600;font-size:12px;line-height:15px}
.foot-blurb{position:absolute;left:57px;top:108px;width:123px;font-size:7.4px;line-height:11px;font-family:"Raleway",sans-serif}
.foot-head{position:absolute;top:57px;font-size:11.5px;font-weight:400;letter-spacing:.2px}
.contact-row{position:absolute;left:214px;font-size:9.5px;line-height:11.5px}
.contact-row svg{position:absolute;left:0;top:0}
.contact-row span{position:absolute;left:21px;top:0;white-space:nowrap}
.foot-links{position:absolute;left:385px;top:88px;font-size:9.5px;line-height:20px;list-style:none}
.field{position:absolute;height:24px;background:var(--white);color:var(--grey);font-size:8px;line-height:24px;padding-left:8px}
.send{position:absolute;left:517px;top:138px;width:82px;height:24px;background:var(--ink);color:var(--white);font-family:"Montserrat",sans-serif;font-weight:600;font-size:10px;text-align:center;line-height:24px}
.copyright{position:absolute;left:0;top:1153px;width:755px;height:47px;background:var(--footer-bar);color:#ddd;font-size:7.6px;text-align:center;line-height:47px;font-family:"Raleway",sans-serif}
</style>
</head>
<body>

<header class="site-header">
  <div class="brand">Fernwick Hollow<br>Craft Cannabis</div>
  <nav class="main-nav">
    <a class="active" style="left:317px">Home</a>
    <a style="left:377px">Investors</a>
    <a style="left:448px">Our mission</a>
    <a style="left:532px">Values and visions</a>
  </nav>
  <div class="shop-btn">SHOP NOW</div>
</header>

<section class="hero" role="img" aria-label="Photo of a long greenhouse tunnel with rows of green plants">
  <div class="hero-text hero-welcome">Welcome to</div>
  <h1 class="hero-text hero-title">Fernwick Hollow Craft Cannabis Company</h1>
  <div class="hero-text hero-sub">High quality handcrafted cannabis</div>
  <div class="hero-text hero-status">COMING SOON</div>
  <div class="dots">
    <span class="dot on" style="left:0"></span>
    <span class="dot" style="left:12px"></span>
    <span class="dot" style="left:25px"></span>
  </div>
</section>

<h2 class="about-title">About Us</h2>
<div class="about-rule"></div>
<div class="about-photo" role="img" aria-label="Photo of two scientists in lab coats inspecting seedlings in a greenhouse"></div>
<div class="about-copy">
  <p>We are located on 20 acres in Marrow Bay, Cedar Valley on lush green acreage. We take pride in our modern technology bloom rooms to contain a healthy environment for high-quality hand-crafted cannabis.</p>
  <p>Lorem ipsum dolor sit amet, consectetur adipiscing elit. Quid autem habent admirationis, cum prope accesseris? An hoc usque quaque, aliter in vita? Non igitur de improbo, sed de callido improbo quaerimus, qualis Q.</p>
</div>
<div class="read-more">Read More</div>

<div class="grass" role="img" aria-label="Silhouette of a grass edge"></div>

<footer class="site-footer">
  <div class="foot-brand">Fernwick Hollow<br>Craft Cannabis</div>
  <p class="foot-blurb">Lorem ipsum dolor sit amet, consectetur adipiscing elit. Morbi auctor ullamcorper congue. Phasellus quis lacus quis ante ornare tincidunt lobortis quisenim.</p>

  <h3 class="foot-head" style="left:214px">CONTACT US</h3>
  <div class="contact-row" style="top:91px">
    <svg width="10" height="14" viewBox="0 0 10 14"><path d="M5 0C2.2 0 0 2.2 0 5c0 3.6 5 9 5 9s5-5.4 5-9C10 2.2 7.8 0 5 0zm0 7.2A2.2 2.2 0 1 1 5 2.8a2.2 2.2 0 0 1 0 4.4z" fill="#fff"/></svg>
    <span>418 Cedarline Rd.<br>Suite 12<br>Marrow Bay, BC V2T 0K4</span>
  </div>
  <div class="contact-row" style="top:136px">
    <svg width="10" height="10" viewBox="0 0 10 10"><path d="M2 0l2 2.5-1 1.3c.6 1.3 1.6 2.3 2.9 2.9L7.2 5.7 10 7.6 9 9.6C4.5 9.8.2 5.5.4 1z" fill="#fff"/></svg>
    <span>800-555-0142</span>
  </div>
  <div class="contact-row" style="top:153px">
    <svg width="10" height="8" viewBox="0 0 10 8" style="top:2px"><rect width="10" height="8" fill="#fff"/><path d="M0 0l5 4 5-4" stroke="#6cc41a" stroke-width="1" fill="none"/></svg>
    <span>hello@fernwickhollow.example</span>
  </div>

  <h3 class="foot-head" style="left:385px">ABOUT US</h3>
  <ul class="foot-links">
    <li>Home</li>
    <li>Investors</li>
    <li>Our mission</li>
    <li>Values and visions</li>
  </ul>

  <h3 class="foot-head" style="left:514px">GET IN TOUCH</h3>
  <div class="field" style="left:517px;top:82px;width:91px">Name</div>
  <div class="field" style="left:611px;top:82px;width:91px">Phone</div>
  <div class="field" style="left:517px;top:110px;width:185px;padding-left:10px">Email address</div>
  <div class="send">SEND</div>
</footer>

<div class="copyright">Copyright © 2017 fernwickhollow - All Rights Reserved</div>

</body>
</html>
```